依頼詳細
国家資格に対応するための新規講習の開講を予定しまして新しいチラシを作成したいと思っております。
令和5年5月リリース予定の新規講習に関しましての広告及び講習に関する説明を行えるチラシのデザインをお願いいたします。
令和5年5月リリース予定ですが、既存の講習受講後に新規講習を追加で受ける形の受講も可能であるため、それまでの間の従来の講習も広告も行っていきたいと思っております。
従来の講習→新規講習の受講の流れを勧めたいです。

利用用途は新聞折込及び、ポスティングにて利用いたします。
希望はA4片面カラーを希望いたします。

納品はpsdファイルおよびPDFファイル(プリモアにすぐに入稿できる仕様)を希望いたします。
記載項目
■校名
ドローン教習所 翠光小樽校・道央MTR校
■空撮技能認定ロゴ

```html
<!DOCTYPE html>
<html lang="ja">
<head>
<meta charset="utf-8">
<title>国家試験コース開講 | ドローン教習所 翠光小樽校・道央MTR校</title>
<link rel="stylesheet" href="https://fonts.googleapis.com/css2?family=M+PLUS+1p:wght@400;700;800;900&family=Noto+Sans+JP:wght@400;700;900&display=swap">
<style>
:root{
  --navy:#0b1f4d;
  --navy-deep:#06122e;
  --blue:#1d4fa8;
  --sky:#2a8fd8;
  --yellow:#ffe000;
  --orange:#f39800;
  --white:#ffffff;
  --ink:#111827;
  --red:#d7141a;
}
*{box-sizing:border-box;margin:0;padding:0}
html,body{width:848px;height:1200px;overflow:hidden;background:var(--white)}
body{font-family:"Noto Sans JP",sans-serif;color:var(--ink)}
.flyer{position:relative;width:848px;height:1200px;overflow:hidden;background:var(--navy)}

.city-night{position:absolute;left:0;top:0;width:848px;height:720px;
  background:radial-gradient(ellipse at 50% 75%,rgba(255,170,60,.55),transparent 55%),
  radial-gradient(ellipse at 80% 60%,rgba(120,180,255,.4),transparent 50%),
  linear-gradient(180deg,#7fb2e0 0%,#2c5d9c 28%,#0e2553 55%,#0a1a3f 100%)}
.drone-photo{position:absolute;right:20px;top:30px;width:470px;height:250px;border-radius:40% 40% 30% 30%;
  background:radial-gradient(ellipse at 50% 55%,#f4f6f8 0%,#c9ced6 40%,rgba(140,150,165,.2) 70%,transparent 72%)}

.brand{position:absolute;left:30px;top:24px;width:190px;height:74px;background:var(--white);
  display:flex;align-items:center;justify-content:center;gap:8px;border-radius:4px}
.brand-mark{width:14px;height:14px;background:var(--blue);border-radius:50%}
.brand-name{font-family:"M PLUS 1p",sans-serif;font-weight:900;font-size:24px;color:var(--blue)}
.notice{position:absolute;right:28px;top:10px;font-size:9px;color:var(--white)}

.targets{position:absolute;left:30px;top:145px;display:flex;flex-direction:column;gap:6px}
.target{background:var(--yellow);color:var(--navy);font-weight:900;font-size:19px;padding:4px 14px;
  transform:skewX(-8deg);box-shadow:3px 3px 0 var(--navy-deep);width:max-content}

.headline{position:absolute;left:0;top:250px;width:848px;text-align:center;font-family:"M PLUS 1p",sans-serif;
  font-weight:900;font-size:98px;color:var(--yellow);letter-spacing:2px;
  -webkit-text-stroke:4px var(--navy-deep);paint-order:stroke fill;text-shadow:0 5px 0 var(--navy-deep)}
.open{position:absolute;left:22px;top:370px;font-family:"M PLUS 1p",sans-serif;font-weight:900;color:var(--yellow);
  -webkit-text-stroke:4px var(--navy-deep);paint-order:stroke fill}
.open-school{font-size:30px;color:var(--white);display:block;-webkit-text-stroke:0;text-shadow:2px 2px 0 var(--navy-deep)}
.open-word{font-size:120px;line-height:1;display:block}
.school-big{position:absolute;left:232px;top:382px;font-weight:900;font-size:36px;color:var(--white);text-shadow:2px 2px 0 var(--navy-deep)}
.lead{position:absolute;left:440px;top:440px;width:380px;font-size:14px;line-height:1.65;color:var(--white);font-weight:700}

.start{position:absolute;left:180px;top:610px;width:488px;height:50px;background:var(--white);color:var(--navy);
  font-weight:900;font-size:25px;text-align:center;line-height:50px;border-radius:4px}
.start em{font-style:normal;color:var(--blue)}

.flow{position:absolute;left:18px;top:690px;width:812px;display:flex;align-items:center;gap:6px}
.step{background:var(--white);border:3px solid var(--blue);border-radius:6px;text-align:center;padding:8px 6px;color:var(--navy)}
.step-label{font-size:11px;font-weight:700;background:var(--blue);color:var(--white);padding:2px 4px;border-radius:3px}
.step-title{font-size:17px;font-weight:900;margin-top:4px}
.price{font-family:"M PLUS 1p",sans-serif;font-weight:900;font-size:32px;color:var(--red);line-height:1.1}
.price small{font-size:15px}
.step-note{font-size:10px;margin-top:3px}
.step-wide{width:230px}
.step-mid{width:130px;background:var(--yellow);border-color:var(--yellow);font-weight:900;font-size:16px;line-height:1.4;padding:22px 8px}
.step-end{width:120px;background:#e8eef8;font-weight:900;font-size:14px;line-height:1.5;padding:22px 6px}
.arrow{width:22px;height:40px;flex:none}

.content{position:absolute;left:30px;top:880px;width:788px}
.content-title{width:max-content;margin:0 auto 10px;background:var(--white);color:var(--navy);font-weight:900;font-size:20px;padding:4px 24px;border-radius:3px}
.content-text{font-size:13px;line-height:1.7;color:var(--white)}

.footer{position:absolute;left:0;top:1020px;width:848px;height:180px;background:var(--white);padding:22px 30px}
.contact-lead{display:inline-block;background:var(--navy);color:var(--white);font-weight:700;font-size:14px;padding:3px 14px}
.footer-school{font-weight:900;font-size:22px;color:var(--navy);margin-top:8px}
.footer-row{display:flex;align-items:center;gap:24px;margin-top:6px}
.tel{font-family:"M PLUS 1p",sans-serif;font-weight:900;font-size:38px;color:var(--navy);display:flex;align-items:center;gap:8px}
.web{font-size:13px;line-height:1.8;color:var(--ink)}
.web div{display:flex;align-items:center;gap:6px}
</style>
</head>
<body>
<main class="flyer">
  <div class="city-night" role="img" aria-label="夜景の街並みを見下ろす空撮写真"></div>
  <div class="drone-photo" role="img" aria-label="夜空を飛ぶ白いドローンの写真"></div>

  <div class="brand"><span class="brand-mark"></span><span class="brand-name">空撮技能認定</span></div>
  <p class="notice">「空撮技能認定」の名称は登録商標として管理しています。</p>

  <div class="targets">
    <p class="target">基礎技能講習受講済の方</p>
    <p class="target">ドローン操縦士として活躍したい方</p>
    <p class="target">ドローン操縦士ライセンスを取得したい方</p>
  </div>

  <h1 class="headline">国家試験コース</h1>
  <p class="open"><span class="open-school">ドローン教習所</span><span class="open-word">開講!</span></p>
  <p class="school-big">翠光小樽校・道央MTR校</p>
  <p class="lead">登録講習機関に登録したドローン教習所で実施する無人航空機操縦者技能証明（ドローン操縦士ライセンス）取得に対応した講習です。講習を修了すると「指定試験機関」が実施する「無人航空機操縦士試験」での「実地試験」が免除されます。</p>

  <p class="start">まずは<em>「基礎技能講習」</em>からスタート!</p>

  <div class="flow">
    <div class="step step-wide">
      <span class="step-label">空撮技能認定 受講料</span>
      <p class="step-title">基礎技能講習</p>
      <p class="price">99,000円<small>(税込)</small></p>
      <p class="step-note">学科講習6時間 実地講習10時間</p>
      <p class="step-note">空撮技能認定3級以上を取得</p>
    </div>
    <svg class="arrow" viewBox="0 0 22 40"><path d="M2 2 L20 20 L2 38 Z" fill="var(--yellow)"/></svg>
    <div class="step step-mid">3時間以上の<br>実機飛行<br>実績</div>
    <svg class="arrow" viewBox="0 0 22 40"><path d="M2 2 L20 20 L2 38 Z" fill="var(--yellow)"/></svg>
    <div class="step step-wide">
      <span class="step-label">基礎技能講習修了者の方対象</span>
      <p class="step-title">国家試験講習</p>
      <p class="price">112,200円<small>(税込)</small></p>
      <p class="step-note">学科講習4時間 実地講習10時間</p>
    </div>
    <svg class="arrow" viewBox="0 0 22 40"><path d="M2 2 L20 20 L2 38 Z" fill="var(--yellow)"/></svg>
    <div class="step step-end">指定試験機関<br>にて学科試験<br>及び身体検査</div>
  </div>

  <section class="content">
    <h2 class="content-title">「国家試験講習」内容</h2>
    <p class="content-text">学科講習・実地講習があり、実地講習ではシミュレーター訓練と実機訓練があります。ドローン教習所で基礎技能講習を受講した方は（プラス3時間以上の実機飛行実績も必要です）学科講習、実地講習の一部が受講免除となります。</p>
  </section>

  <footer class="footer">
    <p class="contact-lead">お申し込み・お問い合わせはこちらから</p>
    <p class="footer-school">ドローン教習所 翠光小樽校・道央MTR校</p>
    <div class="footer-row">
      <p class="tel">
        <svg width="30" height="30" viewBox="0 0 24 24"><path fill="var(--navy)" d="M6.6 10.8a15 15 0 0 0 6.6 6.6l2.2-2.2c.3-.3.7-.4 1-.2 1.1.4 2.3.6 3.6.6.6 0 1 .4 1 1V20c0 .6-.4 1-1 1A17 17 0 0 1 3 4c0-.6.4-1 1-1h3.5c.6 0 1 .4 1 1 0 1.3.2 2.5.6 3.6.1.3 0 .7-.2 1z"/></svg>
        TEL 0134-62-0815
      </p>
      <div class="web">
        <div><svg width="14" height="14" viewBox="0 0 24 24"><rect x="2" y="5" width="20" height="14" rx="2" fill="none" stroke="var(--navy)" stroke-width="2"/><path d="M2 6l10 7 10-7" fill="none" stroke="var(--navy)" stroke-width="2"/></svg>info-drone@suiko-g.jp</div>
        <div><svg width="14" height="14" viewBox="0 0 24 24"><circle cx="12" cy="12" r="9" fill="none" stroke="var(--navy)" stroke-width="2"/><path d="M3 12h18M12 3c3 3 3 15 0 18M12 3c-3 3-3 15 0 18" fill="none" stroke="var(--navy)" stroke-width="1.5"/></svg>http://www.suiko-g.jp/drone</div>
      </div>
    </div>
  </footer>
</main>
</body>
</html>
```